Medical Services company. Need a website that blows the competition out of the water

We need a web site designed to draw attention to our many services offered. We are a Medical Services business based out of Pennsylvania. We provide basic first aid staffing for events and businesses such as but not limited to: Fairs, Festivals, Carnivals, Sporting events, Large gatherings where a first aid station is needed, Concerts, Businesses with first aid needs . We provide training and certifications that are tailored to the customers needs. We provide Covid-19 pre screening and temperature monitoring. Our professionals consist of individuals with Basic First Aid, Certified Nursing Assistants, Medical Assistants, Emergency Medical Responders (EMR), Emergency Medical Technicians (EMT), and Nurses. I do not know how many pages I will need since we offer multiple different services. Our main services provided are: First Aid services, Covid-19 pre screen and temperatures, and Training/Certifications. You will have to use stock photos for now until I can get some actual photographs of our team.I have uploaded a copy of my brochure so you can get some information from there as well.

Target Market(s)

-For the first Aid and Covid-19 services: All Businesses, Sporting events, Event organizers
-Training: Everyone.

Coding

Number of Pages Required

Font styles to use
Sans Serif

Requirements
Must have
• My colors are what is in the logos and Gray , need to have a way for customers to request a quote, design that grabs their attention. Should have pictures of medical providers attending to the sick or injured. Both in a office setting and in an emergency out in public. Should have pictures of an ambulance. Should also have pictures of staff taking temperatures and asking pre screening questions.
Nice to have
• I'll get back to you on that one

```html
<!DOCTYPE html>
<html lang="en">
<head>
<meta charset="utf-8">
<title>Keystone Medical Services</title>
<link href="https://fonts.googleapis.com/css2?family=Poppins:wght@400;500;600;700;800&display=swap" rel="stylesheet">
<style>
:root{
  --navy:#2b3990;
  --teal:#1bb09a;
  --grey-bg:#f5f5f5;
  --text:#3a3a3a;
  --muted:#7a7a7a;
  --dark:#1c2030;
  --white:#ffffff;
}
*{margin:0;padding:0;box-sizing:border-box}
html,body{width:1200px;height:3527px;overflow:hidden}
body{position:relative;font-family:'Poppins',sans-serif;color:var(--text);background:var(--white)}
.abs{position:absolute}
.btn{position:absolute;display:flex;align-items:center;justify-content:center;background:var(--teal);color:var(--white);font-weight:600;font-size:15px;border-radius:22px;height:41px;width:188px;letter-spacing:.3px}
.section-title{position:absolute;left:0;width:1200px;text-align:center;color:var(--navy);font-weight:800;font-size:35px;letter-spacing:.5px}
/* header */
.site-header{position:absolute;top:0;left:0;width:1200px;height:81px;border-top:2px solid var(--teal);background:var(--white)}
.brand{position:absolute;left:162px;top:22px;display:flex;align-items:center;gap:8px;color:var(--navy);font-weight:700;font-size:22px}
.brand-dot{width:30px;height:30px;border-radius:50%;background:var(--navy)}
.main-nav{position:absolute;top:32px;font-size:14px;color:var(--text)}
.header-phone{position:absolute;left:896px;top:28px;display:flex;align-items:center;gap:10px;font-weight:600;font-size:14px;color:var(--text)}
/* hero */
.hero-photo{position:absolute;top:81px;left:0;width:1200px;height:600px;background:linear-gradient(120deg,#6d7a6a 0%,#3e4a52 40%,#4a5a70 65%,#b4a540 90%)}
.hero-shade{position:absolute;top:81px;left:0;width:1200px;height:600px;background:rgba(0,0,0,.25)}
.hero-title{position:absolute;top:265px;left:0;width:1200px;text-align:center;color:var(--white);font-weight:700;font-size:41px;line-height:50px;letter-spacing:1px}
.hero-wave{position:absolute;top:480px;left:0}
/* about */
.about-text{position:absolute;text-align:center;font-size:14px;line-height:24px;color:var(--text)}
/* services */
.services{position:absolute;top:1064px;left:0;width:1200px;height:574px;background:var(--grey-bg)}
.service{position:absolute;top:1280px;width:180px;text-align:center}
.service-icon{height:70px;display:flex;justify-content:center;align-items:center}
.service h3{margin-top:18px;color:var(--navy);font-size:14px;font-weight:600}
.service p{margin-top:10px;font-size:12px;line-height:15px;color:var(--muted)}
/* first aid */
.lead-title{position:absolute;left:162px;top:1788px;width:440px;color:var(--navy);font-weight:600;font-size:19px;line-height:29px}
.check-item{position:absolute;display:flex;align-items:center;gap:8px;font-size:14px;color:var(--text)}
.photo-ring{position:absolute;border:2px solid var(--navy);border-radius:50%}
.photo{position:absolute;border-radius:50%}
.photo-small{position:absolute;border-radius:50%;border:8px solid var(--white)}
/* training */
.training-title{position:absolute;left:604px;top:2222px;color:var(--navy);font-weight:800;font-size:35px}
.training-body{position:absolute;left:604px;top:2274px;width:430px}
.training-body p{font-size:13.5px;line-height:20px;color:var(--text);margin-bottom:14px}
/* map + footer */
.map-area{position:absolute;top:2685px;left:0;width:1200px;height:520px;background:linear-gradient(135deg,#e7e7e7,#d4d4d4 50%,#e2e2e2)}
.map-card{position:absolute;left:525px;top:2815px;width:150px;height:69px;background:var(--white);border-radius:4px;box-shadow:0 2px 8px rgba(0,0,0,.2);display:flex;align-items:center;justify-content:center;color:var(--navy);font-weight:700;font-size:17px}
.footer-dark{position:absolute;top:3180px;left:0;width:1200px;height:307px;background:var(--dark)}
.footer-wave{position:absolute;top:3015px;left:0}
.footer-nav{position:absolute;top:3240px;color:var(--white);font-size:14px}
.footer-brand{position:absolute;left:540px;top:3205px;width:120px;height:100px;display:flex;flex-direction:column;align-items:center;justify-content:center;gap:6px;color:var(--white);font-weight:700;font-size:15px}
.footer-brand span.dot{width:40px;height:40px;border-radius:50%;background:var(--navy)}
.contact-icon{position:absolute;top:3333px;width:54px;height:54px;border:2px solid var(--teal);border-radius:50%;display:flex;align-items:center;justify-content:center}
.contact-text{position:absolute;top:3406px;width:240px;text-align:center;color:var(--white);font-size:14px;line-height:18px}
.copyright-bar{position:absolute;top:3487px;left:0;width:1200px;height:40px;background:var(--navy)}
.copyright-bar p{position:absolute;left:162px;top:11px;color:var(--white);font-size:13px}
.social{position:absolute;top:14px;width:12px;height:12px;border-radius:50%;background:var(--white)}
</style>
</head>
<body>

<header class="site-header">
  <div class="brand"><span class="brand-dot"></span>Keystone</div>
  <nav>
    <span class="main-nav" style="left:497px">Home</span>
    <span class="main-nav" style="left:580px">About Us</span>
    <span class="main-nav" style="left:683px">Services</span>
    <span class="main-nav" style="left:782px">Contact Us</span>
  </nav>
  <div class="header-phone">
    <svg width="22" height="22" viewBox="0 0 24 24" fill="none" stroke="#1bb09a" stroke-width="1.8"><path d="M5 3h4l2 5-2.5 1.5a11 11 0 0 0 6 6L16 13l5 2v4a2 2 0 0 1-2 2A16 16 0 0 1 3 5a2 2 0 0 1 2-2z"/></svg>
    +1 555 014 2290
  </div>
</header>

<section class="hero">
  <div class="hero-photo" role="img" aria-label="Paramedics in reflective jackets attending to a patient outdoors"></div>
  <div class="hero-shade"></div>
  <h1 class="hero-title">PROVIDING ALL OF YOUR HEALTH<br>AND SAFETY NEEDS</h1>
  <div class="btn" style="left:510px;top:381px;width:180px">CALL US TODAY</div>
  <svg class="hero-wave" width="1200" height="205" viewBox="0 0 1200 205">
    <path d="M0 165 C150 50 360 0 620 70 S1060 205 1200 120 L1200 205 L0 205 Z" fill="#2b3990"/>
    <path d="M0 205 C200 75 420 40 640 100 S1070 200 1200 128 L1200 205 Z" fill="#ffffff"/>
  </svg>
</section>

<section class="about">
  <h2 class="section-title" style="top:710px">ABOUT KEYSTONE MEDICAL SERVICES</h2>
  <p class="about-text" style="top:766px;left:232px;width:736px;line-height:21px">Lorem ipsum dolor sit amet, constetuer adipiscing diam nonummy nibh euismod tincidunt elit, sed laoreet dolore &nbsp;qui nostrud exerci tation ullamcorper suscipit lobortis nisl aliquip ex ea</p>
  <p class="about-text" style="top:820px;left:205px;width:790px">Lorem ipsum dolor sit amet, consectetuer adipiscing elit, sed diam nonummy nibh euismod tincidunt ut laoreet dolore magna aliquam erat volutpat. Ut wisi enim ad minim veniam, qui nostrud exerci tation ullamcorper suscipit lobortis nisl aliquip ex ea commodo consequat. Duis autem veum iriure dolor hendrerit</p>
  <div class="btn" style="left:525px;top:911px;width:150px">READ MORE</div>
</section>

<section class="services"></section>
<h2 class="section-title" style="top:1165px">OUR SERVICES</h2>
<p class="abs" style="top:1217px;left:0;width:1200px;text-align:center;font-size:14px">Lorem ipsum dolor sit amet, constetuer adipiscing diam nonummy</p>

<div class="service" style="left:176px">
  <div class="service-icon"><svg width="60" height="56" viewBox="0 0 60 56"><rect x="20" y="2" width="20" height="10" rx="2" fill="none" stroke="#2b3990" stroke-width="4"/><rect x="0" y="10" width="60" height="46" rx="6" fill="#2b3990"/><path d="M26 22h8v8h8v8h-8v8h-8v-8h-8v-8h8z" fill="#fff"/></svg></div>
  <h3>First Aid</h3>
  <p>For patients with minor to life threatening injuries or illness</p>
</div>
<div class="service" style="left:398px">
  <div class="service-icon"><svg width="58" height="58" viewBox="0 0 58 58" fill="none" stroke="#2b3990" stroke-width="3"><circle cx="31" cy="31" r="22"/><path d="M31 4v5M27 4h8"/><path d="M31 20v11l8 6"/><path d="M2 27h14M5 33h12M2 39h10" stroke-width="2.5"/></svg></div>
  <h3>Onsite Care</h3>
  <p>Provide immediate care by removing the delay in response, assessment and treatment</p>
</div>
<div class="service" style="left:621px">
  <div class="service-icon"><svg width="64" height="60" viewBox="0 0 64 60"><path d="M32 58 C10 40 0 28 0 16 A16 16 0 0 1 32 10 A16 16 0 0 1 64 16 C64 28 54 40 32 58z" fill="#2b3990"/><path d="M35 10 L24 32 H32 L27 50 L42 26 H34 L38 10z" fill="#fff"/></svg></div>
  <h3>Trauma/Resuscitation</h3>
  <p>Provide Immediate and LIFE SAVING treatment for patients with Life Threatening injuries or illness</p>
</div>
<div class="service" style="left:846px">
  <div class="service-icon"><svg width="68" height="60" viewBox="0 0 68 60" fill="#2b3990"><circle cx="20" cy="38" r="12"/><circle cx="46" cy="14" r="9"/><circle cx="52" cy="40" r="7"/><circle cx="6" cy="26" r="2.5"/><circle cx="34" cy="32" r="2.5"/><circle cx="30" cy="50" r="2.5"/><circle cx="58" cy="6" r="2"/><circle cx="36" cy="8" r="2"/></svg></div>
  <h3>Covid-19 Pre Screening</h3>
  <p>Pre Screening and Temperature Monitoring of Individuals entering your facility or event</p>
</div>
<div class="btn" style="left:506px;top:1490px">CALL US TODAY</div>

<section class="coverage">
  <h2 class="lead-title">We provide basic first aid and covid-19 pre screening and temperature monitoring for, but not limited to:</h2>
  <div class="check-item" style="left:162px;top:1901px"><svg width="12" height="10" viewBox="0 0 12 10"><path d="M1 5l3.5 3.5L11 1" stroke="#1bb09a" stroke-width="2.2" fill="none"/></svg>Special Events</div>
  <div class="check-item" style="left:162px;top:1935px"><svg width="12" height="10" viewBox="0 0 12 10"><path d="M1 5l3.5 3.5L11 1" stroke="#1bb09a" stroke-width="2.2" fill="none"/></svg>Large Gatherings</div>
  <div class="check-item" style="left:162px;top:1969px"><svg width="12" height="10" viewBox="0 0 12 10"><path d="M1 5l3.5 3.5L11 1" stroke="#1bb09a" stroke-width="2.2" fill="none"/></svg>Businesses</div>
  <div class="check-item" style="left:162px;top:2003px"><svg width="12" height="10" viewBox="0 0 12 10"><path d="M1 5l3.5 3.5L11 1" stroke="#1bb09a" stroke-width="2.2" fill="none"/></svg>Sporting Events</div>
  <div class="check-item" style="left:333px;top:1901px"><svg width="12" height="10" viewBox="0 0 12 10"><path d="M1 5l3.5 3.5L11 1" stroke="#1bb09a" stroke-width="2.2" fill="none"/></svg>Manufacturing Facilities</div>
  <div class="check-item" style="left:333px;top:1935px"><svg width="12" height="10" viewBox="0 0 12 10"><path d="M1 5l3.5 3.5L11 1" stroke="#1bb09a" stroke-width="2.2" fill="none"/></svg>Industrial Buildings</div>
  <div class="check-item" style="left:333px;top:1969px"><svg width="12" height="10" viewBox="0 0 12 10"><path d="M1 5l3.5 3.5L11 1" stroke="#1bb09a" stroke-width="2.2" fill="none"/></svg>Large Construction Sites</div>
  <div class="check-item" style="left:333px;top:2003px"><svg width="12" height="10" viewBox="0 0 12 10"><path d="M1 5l3.5 3.5L11 1" stroke="#1bb09a" stroke-width="2.2" fill="none"/></svg>Multi Occupancy Office Buildings</div>
  <div class="btn" style="left:162px;top:2057px">CALL US TODAY</div>

  <div class="photo-ring" style="left:688px;top:1748px;width:362px;height:362px"></div>
  <div class="photo" style="left:700px;top:1760px;width:338px;height:338px;background:linear-gradient(135deg,#c9c9c9,#9a8e80 45%,#2e3650)" role="img" aria-label="Staff member in a face mask having her temperature taken"></div>
  <div class="photo-small" style="left:659px;top:1944px;width:194px;height:194px;background:linear-gradient(160deg,#e9eef4,#9fb0c4 60%,#5a6a50)" role="img" aria-label="White ambulance parked outside"></div>
</section>

<section class="training">
  <div class="photo-ring" style="left:147px;top:2204px;width:364px;height:364px"></div>
  <div class="photo" style="left:160px;top:2217px;width:338px;height:338px;background:linear-gradient(135deg,#e4e2de,#b9a996 50%,#5b6470)" role="img" aria-label="Trainee practising chest compressions on a CPR manikin"></div>
  <div class="photo-small" style="left:347px;top:2410px;width:184px;height:184px;background:linear-gradient(160deg,#7f9a5a,#c23a35 50%,#3c4a2e)" role="img" aria-label="Medical kit bags on grass at an outdoor event"></div>

  <h2 class="training-title">TRAINING SERVICES</h2>
  <div class="training-body">
    <p>At Keystone we have a broad range of Health and Safety classes to suit your every need. We take pride in our instructors who have years of experience instructing quality built classes.</p>
    <p>We make learning CPR fun and affordable for the everyday public and healthcare providers.</p>
    <p>All CPR instruction follows the National Cardiac Council and Allied Safety Training Institute formats. The leaders in cardiac research.</p>
    <p>We can adjust any course format to suit your CPR and First Aid needs.</p>
  </div>
  <div class="btn" style="left:602px;top:2539px">CALL US TODAY</div>
</section>

<section class="location">
  <div class="map-area" role="img" aria-label="Greyscale map of Pennsylvania showing the office location"></div>
  <div class="map-card">Keystone</div>
  <svg class="abs" style="left:546px;top:2908px" width="18" height="24" viewBox="0 0 18 24"><path d="M9 23C3 15 1 12 1 8a8 8 0 0 1 16 0c0 4-2 7-8 15z" fill="#e02424"/><circle cx="9" cy="8" r="3" fill="#fff"/></svg>
</section>

<footer>
  <svg class="footer-wave" width="1200" height="170" viewBox="0 0 1200 170">
    <path d="M0 150 C180 30 430 -10 660 70 S1060 175 1200 120 L1200 170 L0 170 Z" fill="#2b3990"/>
    <path d="M0 166 C200 50 440 12 670 88 S1070 182 1200 134 L1200 170 L0 170 Z" fill="#1c2030"/>
  </svg>
  <div class="footer-dark" role="img" aria-label="City skyline at night"></div>
  <nav>
    <span class="footer-nav" style="left:335px">Home</span>
    <span class="footer-nav" style="left:445px">About Us</span>
    <span class="footer-nav" style="left:690px">Services</span>
    <span class="footer-nav" style="left:817px">Contact Us</span>
  </nav>
  <div class="footer-brand"><span class="dot"></span>Keystone</div>

  <div class="contact-icon" style="left:289px"><svg width="24" height="26" viewBox="0 0 24 26" fill="none" stroke="#fff" stroke-width="1.6"><path d="M12 24C5 16 4 13 4 10a8 8 0 0 1 16 0c0 3-1 6-8 14z"/><circle cx="12" cy="10" r="3"/></svg></div>
  <div class="contact-icon" style="left:569px"><svg width="24" height="24" viewBox="0 0 24 24" fill="none" stroke="#fff" stroke-width="1.6"><path d="M5 3h4l2 5-2.5 1.5a11 11 0 0 0 6 6L16 13l5 2v4a2 2 0 0 1-2 2A16 16 0 0 1 3 5a2 2 0 0 1 2-2z"/></svg></div>
  <div class="contact-icon" style="left:847px"><svg width="26" height="22" viewBox="0 0 26 22" fill="none" stroke="#fff" stroke-width="1.6"><rect x="2" y="4" width="22" height="16" rx="1"/><path d="M2 5l11 8 11-8"/></svg></div>
  <p class="contact-text" style="left:196px">Lorem Ipsum Dolor, Giam<br>Adipiscing - 36589</p>
  <p class="contact-text" style="left:476px;font-weight:600">+1 555 014 2290</p>
  <p class="contact-text" style="left:754px">info@keystonemedserv.com</p>

  <div class="copyright-bar">
    <p>Copyright © 2020 Keystone Medical Services. All Rights Reserved.</p>
    <span class="social" style="left:952px"></span>
    <span class="social" style="left:973px"></span>
    <span class="social" style="left:997px"></span>
    <span class="social" style="left:1024px"></span>
  </div>
</footer>

</body>
</html>
```